Larrowby Tavern

I am seeking a draft rack card for a client. Please NOTE - I only have FPO low res pix at this point...would send hi res pix if I get the job. The Tavern wants a "warm" feeling to convey the "Catskill Mountain comfort food" that it specializes in. It's not vital to use all of the images included, but wanted to offer a choice.

```html
<!DOCTYPE html>
<html lang="en">
<head>
<meta charset="utf-8">
<title>Larrowby Tavern – Rack Card</title>
<link href="https://fonts.googleapis.com/css2?family=Merriweather:ital,wght@0,700;0,900;1,700&family=Roboto:wght@400;500;700&family=Open+Sans:ital,wght@0,400;1,700&family=Caveat:wght@500&display=swap" rel="stylesheet">
<style>
  :root {
    --canvas: #e2e2e2;
    --cream: #fbefd6;
    --brown: #4a230f;
    --gold-line: #c9a24a;
    --red: #a82024;
    --gold: #e5ae35;
    --ink: #2b2b2b;
    --wine: #5a1414;
    --black: #0a0a0a;
    --white: #ffffff;
  }
  * { box-sizing: border-box; margin: 0; padding: 0; }
  html, body { width: 1200px; height: 1200px; overflow: hidden; background: var(--canvas); }
  .canvas { position: relative; width: 1200px; height: 1200px; }

  .card {
    position: absolute; top: 258px; width: 323px; height: 684px;
    display: flex; flex-direction: column; background: var(--white);
  }
  .card--front { left: 210px; }
  .card--back { left: 666px; }

  .header {
    flex: 0 0 auto;
    background: var(--cream); display: flex; align-items: center; justify-content: center;
    gap: 8px; border-bottom: 8px solid var(--brown);
  }
  .card--front .header { height: 126px; }
  .card--back .header { height: 112px; border-bottom-width: 6px; }
  .brand-dot { width: 12px; height: 12px; border-radius: 50%; background: var(--brown); }
  .brand-name {
    font-family: "Merriweather", serif; font-weight: 700; color: var(--brown);
    font-size: 19px; letter-spacing: 1.5px;
  }
  .card--back .brand-name { font-size: 16px; }

  .photo { display: block; }
  .photo--dining {
    flex: 0 0 262px; border-top: 1px solid var(--gold-line); border-bottom: 2px solid var(--gold-line);
    background: linear-gradient(180deg, #d9d3c8 0%, #6b4a33 35%, #3a2417 70%, #2a170d 100%);
  }
  .photo-row { display: flex; flex: 0 0 150px; border-bottom: 2px solid var(--gold-line); }
  .photo--burger { flex: 0 0 158px; border-right: 2px solid var(--gold-line);
    background: linear-gradient(160deg, #4a5560 0%, #6b3a25 50%, #2b2420 100%); }
  .photo--cheesecake { flex: 1;
    background: linear-gradient(160deg, #5a3b2a 0%, #e9e1cf 55%, #c9bba2 100%); }

  .title-band {
    flex: 0 0 auto;
    background: var(--red); color: var(--white); text-align: center;
    font-family: "Merriweather", serif; display: flex; flex-direction: column; justify-content: center;
  }
  .card--front .title-band { height: 90px; padding-top: 24px; border-bottom: 10px solid var(--brown); }
  .card--back .title-band { height: 72px; margin-top: 6px; }
  .title-band__name { font-weight: 700; font-size: 21px; letter-spacing: 0.5px; line-height: 1.15; }
  .title-band__sub { font-style: italic; font-weight: 700; font-size: 13.5px; letter-spacing: 0.3px; }

  .tagline {
    flex: 0 0 70px; display: flex; align-items: center; justify-content: center;
    font-family: "Caveat", cursive; font-weight: 500; font-size: 26px; color: var(--wine);
    white-space: nowrap; text-align: center;
  }

  .contact {
    flex: 0 0 auto;
    background: var(--gold); font-family: "Roboto", sans-serif; color: var(--ink);
  }
  .contact__script { font-family: "Caveat", cursive; font-weight: 500; color: var(--red); }
  .card--front .contact { height: 98px; text-align: center; padding-top: 8px; line-height: 1.2; }
  .card--front .contact__script { font-size: 26px; line-height: 1; }
  .contact__phone { font-weight: 700; font-size: 15px; }
  .contact__line { font-size: 12.5px; }

  .about {
    flex: 1; padding: 22px 24px 0 23px; font-family: "Open Sans", sans-serif;
    font-size: 9.4px; line-height: 1.3; color: var(--ink); text-align: justify;
  }
  .about p + p { margin-top: 12px; }
  .about em { font-weight: 700; }

  .card--back .contact {
    height: 58px; display: flex; justify-content: space-between; align-items: center; padding: 0 24px 0 23px;
  }
  .card--back .contact__script { font-size: 22px; line-height: 1; }
  .contact__col { display: flex; flex-direction: column; gap: 2px; }
  .contact__item { display: flex; align-items: flex-start; gap: 4px; font-size: 11px; line-height: 1.2; }
  .contact__item--phone { font-weight: 700; font-size: 13px; align-items: center; }
  .icon { width: 9px; height: 9px; flex: 0 0 9px; margin-top: 2px; }
  .contact__item--phone .icon { margin-top: 0; }

  .foot { background: var(--black); flex: 1 0 24px; }
</style>
</head>
<body>
<div class="canvas">

  <section class="card card--front">
    <header class="header">
      <span class="brand-dot"></span>
      <span class="brand-name">LARROWBY TAVERN</span>
    </header>
    <div class="photo photo--dining" role="img" aria-label="Dining room with wooden coffered ceiling, tables and two red cocktails with orange slices"></div>
    <div class="title-band">
      <span class="title-band__name">LARROWBY TAVERN –</span>
      <span class="title-band__sub">ALDERBROOK RESTAURANT &amp; BAR</span>
    </div>
    <div class="tagline">Catskill Mountain comfort food</div>
    <div class="contact">
      <div class="contact__script">Larrowby Tavern</div>
      <div class="contact__phone">(845) 555-0142</div>
      <div class="contact__line">larrowbytavern.com</div>
      <div class="contact__line">212 Orchard St Alderbrook, NY 12400</div>
    </div>
    <div class="foot"></div>
  </section>

  <section class="card card--back">
    <header class="header">
      <span class="brand-dot"></span>
      <span class="brand-name">LARROWBY TAVERN</span>
    </header>
    <div class="photo-row">
      <div class="photo photo--burger" role="img" aria-label="Burger with tomato and a side of fries on a dark plate"></div>
      <div class="photo photo--cheesecake" role="img" aria-label="Slice of cheesecake with cream and blueberries"></div>
    </div>
    <div class="title-band">
      <span class="title-band__name">LARROWBY TAVERN</span>
      <span class="title-band__sub">ALDERBROOK RESTAURANT &amp; BAR</span>
    </div>
    <div class="about">
      <p>Larrowby Square, a staple to Alderbrook, has been revived under new ownership as Larrowby Tavern. The tavern is built over the Larrowby and is intended to make you feel comfort after a long day.</p>
      <p>We welcome all to come celebrate a special occasion or spend the evening at Larrowby to experience the spirit of the mountain living and fresh air. Offering a large variety of delectable <em>"Mountain Comfort Food,"</em> which coincides with the theme of the location, decor and local products, along with some longstanding favorites, we are open Thursday to Monday with full bar service.</p>
      <p>Our menu is based on modern interpretations of traditional mountain dishes as well as a Brunch menu that is currently in the works. We are excited to continue to serve the community for decades to come, and offer some of the best food and drinks in the Catskills.</p>
    </div>
    <div class="contact">
      <div class="contact__col">
        <div class="contact__script">Larrowby Tavern</div>
        <div class="contact__item contact__item--phone">
          <svg class="icon" viewBox="0 0 10 10" aria-hidden="true"><circle cx="5" cy="5" r="5" fill="#111"/><rect x="3.4" y="2" width="3.2" height="6" rx="0.8" fill="#e5ae35"/></svg>
          (845) 555-0142
        </div>
      </div>
      <div class="contact__col">
        <div class="contact__item">
          <svg class="icon" viewBox="0 0 10 10" aria-hidden="true"><g fill="none" stroke="#111" stroke-width="0.9"><circle cx="5" cy="5" r="4.4"/><ellipse cx="5" cy="5" rx="2" ry="4.4"/><line x1="0.6" y1="5" x2="9.4" y2="5"/></g></svg>
          larrowbytavern.com
        </div>
        <div class="contact__item">
          <svg class="icon" viewBox="0 0 10 10" aria-hidden="true"><circle cx="5" cy="5" r="5" fill="#111"/><path d="M5 2.2a1.8 1.8 0 0 1 1.8 1.8C6.8 5.4 5 7.8 5 7.8S3.2 5.4 3.2 4A1.8 1.8 0 0 1 5 2.2z" fill="#e5ae35"/></svg>
          <span>212 Orchard St<br>Alderbrook, NY 12400</span>
        </div>
      </div>
    </div>
    <div class="foot"></div>
  </section>

</div>
</body>
</html>
```